Business Management System Providor Needs Upscale Business Card Design

We provide an online Claims Management System to the Insurance Industry called Meridell Casework Suite. Although our core offering is claims management, our system provides full business management features including reporting, invoicing, business trend analysis, etc..
We have a worldwide client base and our system has become known for its reliability, rich feature set, and intuitive design. This being the case we would like our cards to maintain a high level of professionalism. We have a tendency to lean toward a corporate look and feel and we would like to maintain that image.
Current Site: www.meridellcaseworksuite.example
Target Market(s)
Big Business, Insurance Professionals, Corporate Organizations
Industry/Entity Type
Business Management
Look and feel
Each slider illustrates characteristics of the customer's brand and the style your logo design should communicate.

```html
<!DOCTYPE html>
<html lang="en">
<head>
<meta charset="utf-8">
<title>Meridell Casework Suite — Business Card</title>
<link rel="stylesheet" href="https://fonts.googleapis.com/css2?family=Open+Sans:wght@400;600;700;800&display=swap">
<style>
  :root {
    --navy: #123f7c;
    --navy-deep: #0c2f63;
    --navy-glow: #1d4f92;
    --white: #ffffff;
    --paper: #f4f5f7;
    --ink-blue: #1a3f7a;
    --grey-text: #6d7178;
    --backdrop: #e7e3dd;
  }
  * { box-sizing: border-box; margin: 0; padding: 0; }
  html, body { width: 1200px; height: 900px; overflow: hidden; }
  body {
    background: var(--backdrop);
    font-family: "Open Sans", Arial, sans-serif;
    display: flex;
    flex-direction: column;
    align-items: center;
    justify-content: center;
    gap: 44px;
  }
  .card {
    position: relative;
    width: 640px;
    height: 366px;
    border-radius: 4px;
    overflow: hidden;
    box-shadow: 0 10px 26px rgba(0,0,0,0.22);
  }
  .card--front {
    background: radial-gradient(ellipse at 72% 35%, var(--navy-glow) 0%, var(--navy) 55%, var(--navy-deep) 100%);
  }
  .card--back {
    background: radial-gradient(ellipse at 75% 40%, var(--navy-glow) 0%, var(--navy) 55%, var(--navy-deep) 100%);
  }
  .watermark-square {
    position: absolute;
    width: 230px;
    height: 230px;
    border-radius: 34px;
    background: rgba(255,255,255,0.07);
  }
  .card--front .watermark-square { right: 60px; top: 20px; }
  .card--back .watermark-square { right: 50px; top: 40px; }

  .brand { display: flex; align-items: center; gap: 14px; }
  .brand__square {
    width: 74px; height: 74px; border-radius: 12px; flex: none;
  }
  .brand__name {
    font-weight: 800;
    font-size: 25px;
    line-height: 1.02;
    letter-spacing: -0.3px;
  }
  .brand__tagline {
    margin-top: 10px;
    padding-top: 6px;
    font-size: 19px;
    letter-spacing: 0.4px;
  }

  .card--front .brand-block {
    position: absolute; left: 150px; top: 96px;
  }
  .card--front .brand__square { background: rgba(255,255,255,0.85); }
  .card--front .brand__name { color: var(--white); }
  .card--front .brand__tagline {
    color: var(--white);
    border-top: 2px solid rgba(255,255,255,0.7);
    margin-left: 30px;
  }

  .back__panel {
    position: absolute; left: 0; top: 0; bottom: 0;
    width: 250px;
    background: var(--paper);
    border-radius: 0 26px 26px 0;
    padding: 54px 0 0 30px;
  }
  .card--back .brand__square { width: 62px; height: 62px; background: var(--navy); }
  .card--back .brand__name { color: var(--ink-blue); font-size: 20px; }
  .card--back .brand__tagline { color: var(--grey-text); font-size: 15px; margin-top: 4px; padding-top: 2px; border-top: 1px solid #b9bcc2; }
  .address {
    margin-top: 14px;
    margin-left: 22px;
    color: var(--ink-blue);
    font-size: 14px;
    line-height: 1.45;
    text-align: center;
    width: 190px;
  }

  .contact {
    position: absolute; left: 280px; top: 96px;
    color: var(--white);
  }
  .contact__name { font-weight: 700; font-size: 19px; letter-spacing: 0.5px; }
  .contact__role { font-size: 13.5px; margin-bottom: 22px; }
  .contact__list { list-style: none; }
  .contact__item { display: flex; align-items: center; gap: 8px; font-size: 14px; line-height: 1.55; }
  .contact__icon { width: 14px; height: 14px; flex: none; fill: var(--white); }
</style>
</head>
<body>

<section class="card card--front" aria-label="Card front">
  <div class="watermark-square"></div>
  <div class="brand-block">
    <div class="brand">
      <div class="brand__square"></div>
      <div class="brand__name">Meridell<br>Casework<br>Suite</div>
    </div>
    <div class="brand__tagline">claim management systems</div>
  </div>
</section>

<section class="card card--back" aria-label="Card back">
  <div class="watermark-square"></div>
  <div class="back__panel">
    <div class="brand">
      <div class="brand__square"></div>
      <div class="brand__name">Meridell<br>Casework<br>Suite</div>
    </div>
    <div class="brand__tagline">claim management systems</div>
    <address class="address" style="font-style:normal">
      1180 Harlow Crescent West<br>Suite 600<br>Brookvale, ON,<br>Canada, K0L 3R9
    </address>
  </div>

  <div class="contact">
    <div class="contact__name">DANA WHITCOMBE</div>
    <div class="contact__role">Director of Software Development</div>
    <ul class="contact__list">
      <li class="contact__item">
        <svg class="contact__icon" viewBox="0 0 16 16" aria-hidden="true"><path d="M3.5 1l2.5 3-1.5 1.8c.8 1.9 2.2 3.4 4.2 4.3L10.5 8.5l3 2.4-1.3 2.6C6.4 13.3 2.6 9.5 1 3.4z"/></svg>
        555-014-2286 x214
      </li>
      <li class="contact__item">
        <svg class="contact__icon" viewBox="0 0 16 16" aria-hidden="true"><rect x="4" y="1" width="8" height="4"/><rect x="1" y="6" width="14" height="6" rx="1"/><rect x="4" y="10" width="8" height="5" fill="#123f7c" stroke="#fff" stroke-width="1.2"/></svg>
        800-555-0147
      </li>
      <li class="contact__item">
        <svg class="contact__icon" viewBox="0 0 16 16" aria-hidden="true"><rect x="1" y="3" width="14" height="10" rx="1"/><path d="M1.5 3.5L8 9l6.5-5.5" fill="none" stroke="#123f7c" stroke-width="1.4"/></svg>
        dwhitcombe@meridellcaseworksuite.example
      </li>
      <li class="contact__item">
        <svg class="contact__icon" viewBox="0 0 16 16" aria-hidden="true"><g fill="none" stroke="#fff" stroke-width="1.3"><circle cx="8" cy="8" r="6.5"/><ellipse cx="8" cy="8" rx="3" ry="6.5"/><path d="M1.5 8h13M2.5 4.8h11M2.5 11.2h11"/></g></svg>
        www.meridellcaseworksuite.example
      </li>
    </ul>
  </div>
</section>

</body>
</html>
```